Voltarey - Flyer design

Description -
Motorhome and Caravan EWOFs
Recreational Vehicles (such as caravans, motorhomes, RVs, Boats etc) and Relocatable buildings that can be connected to an electricity supply must be regularly checked for electrical safety. An EWOF needs to be issued every 4 years.
Pre-purchase house inspections
A pre-purchase electrical inspection prior to buying a home can be used to identify any dangerous and unsafe electrical parts of the installation that may be costly to repair once the property has been purchased. Giving you peace of mind when buying your new home.
High risk Electrical inspections
All Prescribed Electrical Work that falls under the High Risk category must be inspected by a Registered Electrical Inspector and have a Record of Inspection certificate issued.
Electric Vehicle Chargers
Any electrical vehicle charger that can be accessed by the public (ie in a non-domestic situation) must be periodically inspected and certified every 12 months.
General Electrical Services
Domestic and commercial - We do new builds, Renovations, Maintenance and more!
Dean Fowler - Electrician and Electrical Inspector
Ph - 0227839152
Dean@voltarey.co.nz
Auckland
------
I also want there to be a few symbols similar to the files I have attached.
The main areas that I am hoping to find work is with caravans/motohomes and EV car chargers so these symbols are quite important.
Thanks so much

```html
<!DOCTYPE html>
<html lang="en">
<head>
<meta charset="utf-8">
<title>Voltarey – Flyer</title>
<link href="https://fonts.googleapis.com/css2?family=Antonio:wght@700&family=Russo+One&family=Jost:wght@400;500&display=swap" rel="stylesheet">
<style>
  :root {
    --ink: #000000;
    --volt-green: #8cc63f;
    --panel-grey: #cac6c7;
    --paper: #ffffff;
    --text-dark: #111111;
    --rule: #1a1a1a;
    --photo-dark: #1e2124;
    --photo-mid: #4a5058;
    --photo-warm: #6a3a2c;
  }
  * { box-sizing: border-box; margin: 0; padding: 0; }
  html, body { width: 1200px; height: 1200px; overflow: hidden; background: var(--paper); }
  .flyer {
    position: absolute; left: 200px; top: 0;
    width: 800px; height: 1200px;
    background: var(--ink); overflow: hidden;
    font-family: "Jost", sans-serif;
  }
  .flyer-shapes { position: absolute; inset: 0; }

  .brand {
    position: absolute; left: 18px; top: 58px;
    font-family: "Jost", sans-serif; font-weight: 500; font-size: 34px; line-height: 1;
    color: var(--volt-green); letter-spacing: 0.5px;
  }

  .badge { position: absolute; left: 382px; top: 16px; width: 96px; height: 92px; }
  .hours-number {
    position: absolute; left: 380px; top: 118px;
    font-family: "Antonio", sans-serif; font-weight: 700; font-size: 84px; line-height: 1;
    color: var(--volt-green); letter-spacing: -2px;
  }
  .hours-label {
    position: absolute; left: 447px; top: 193px;
    transform: rotate(-90deg); transform-origin: left top;
    font-family: "Antonio", sans-serif; font-weight: 700; font-size: 32px; line-height: 30px;
    color: var(--volt-green); letter-spacing: 1px;
  }
  .headline {
    position: absolute; left: 502px; top: 50px;
    font-family: "Antonio", sans-serif; font-weight: 700; font-size: 77px; line-height: 72px;
    color: var(--paper); letter-spacing: -2px;
  }

  .section-title {
    position: absolute; font-family: "Russo One", sans-serif; font-size: 34px; line-height: 1;
    text-transform: uppercase;
  }
  .services-title { left: 502px; top: 274px; color: var(--ink); font-size: 35px; }

  .service { position: absolute; color: var(--text-dark); }
  .service-name {
    font-family: "Antonio", sans-serif; font-weight: 700; font-size: 26px; line-height: 32px;
    letter-spacing: -1.3px; color: var(--ink); white-space: nowrap;
  }
  .service-text { font-size: 16.8px; line-height: 20px; margin-top: 4px; white-space: nowrap; }
  .service-icon { position: absolute; fill: none; stroke: var(--ink); stroke-width: 2; stroke-linejoin: round; stroke-linecap: round; }
  .service-rule { position: absolute; height: 2px; background: var(--rule); }

  .about-title { left: 35px; top: 720px; color: var(--volt-green); }
  .about-text {
    position: absolute; left: 35px; top: 763px; width: 229px;
    font-weight: 500; font-size: 15px; line-height: 19.5px; color: var(--paper);
    text-align: justify; text-align-last: center;
  }
  .contact-title { left: 35px; top: 962px; color: var(--volt-green); }
  .contact-details {
    position: absolute; left: 35px; top: 1018px; width: 260px;
    font-weight: 500; font-size: 15px; line-height: 19.5px; color: var(--paper);
  }
  .social { position: absolute; left: 33px; top: 1132px; display: flex; gap: 6px; }
  .social-dot { width: 24px; height: 24px; border-radius: 50%; background: var(--volt-green); display: flex; align-items: center; justify-content: center; }
</style>
</head>
<body>
<main class="flyer">
  <svg class="flyer-shapes" viewBox="0 0 800 1200" width="800" height="1200">
    <polygon class="services-panel" points="500,257 800,257 800,1200 286,1200 286,452" fill="var(--panel-grey)"/>
    <defs>
      <linearGradient id="photo-tone" x1="0" y1="0" x2="1" y2="1">
        <stop offset="0" stop-color="var(--photo-mid)"/>
        <stop offset="0.45" stop-color="var(--photo-warm)"/>
        <stop offset="1" stop-color="var(--photo-dark)"/>
      </linearGradient>
    </defs>
    <polygon class="bolt-photo" role="img" aria-label="Photo: technician's hands holding an electrical diagnostic tester over an engine bay"
      points="0,295 346,0 381,0 308,220 500,255 13,698 0,698 0,665 83,463 0,443"
      fill="url(#photo-tone)" stroke="var(--volt-green)" stroke-width="13" stroke-linejoin="miter"/>
  </svg>

  <div class="brand">Voltarey</div>

  <svg class="badge" viewBox="0 0 100 96">
    <polygon points="50,2 62,34 97,35 69,56 80,92 50,71 20,92 31,56 3,35 38,34" fill="var(--volt-green)" stroke="var(--volt-green)" stroke-width="6" stroke-linejoin="round"/>
    <circle cx="50" cy="50" r="20" fill="var(--paper)"/>
    <polyline points="40,51 47,58 60,43" fill="none" stroke="var(--volt-green)" stroke-width="5" stroke-linecap="round" stroke-linejoin="round"/>
  </svg>
  <div class="hours-number">24</div>
  <div class="hours-label">HOUR</div>
  <h1 class="headline">Excellent<br>Services</h1>

  <h2 class="section-title services-title">Our Services</h2>

  <svg class="service-icon" style="left:374px;top:366px" width="90" height="52" viewBox="0 0 90 52">
    <path d="M14 40 V12 Q14 4 24 4 H80 Q86 4 86 10 V40 Z"/>
    <rect x="20" y="12" width="28" height="12" rx="2"/><line x1="34" y1="12" x2="34" y2="24"/>
    <rect x="64" y="12" width="12" height="26"/>
    <circle cx="40" cy="44" r="6"/><circle cx="40" cy="44" r="2"/>
    <line x1="14" y1="40" x2="2" y2="40"/><line x1="2" y1="36" x2="2" y2="48"/>
  </svg>
  <section class="service" style="left:471px;top:326px">
    <h3 class="service-name">Motorhome and Caravan EWOFs</h3>
    <p class="service-text">Recreational Vehicles (such as caravans,<br>motorhomes, RVs, Boats etc) and<br>Relocatable buildings that can be connected<br>to an electricity supply must be regularly<br>checked for electrical safety. An EWOF<br>needs to be issued every 4 years.</p>
  </section>
  <div class="service-rule" style="left:424px;top:498px;width:349px"></div>

  <svg class="service-icon" style="left:305px;top:543px" width="72" height="70" viewBox="0 0 72 70">
    <path d="M10 32 L36 4 L62 32 M14 28 V66 H58 V28"/>
    <path d="M39 30 L30 45 H38 L33 58 L44 40 H36 Z"/>
  </svg>
  <section class="service" style="left:394px;top:507px">
    <h3 class="service-name">Pre-purchase house</h3>
    <p class="service-text">A pre-purchase electrical inspection prior to<br>buying a home can be used to identify any<br>dangerous and unsafe electrical parts of the<br>installation that may be costly to repair once<br>the property has been purchased. Giving<br>you peace of mind when buying your new<br>home.</p>
  </section>
  <div class="service-rule" style="left:412px;top:693px;width:349px"></div>

  <svg class="service-icon" style="left:404px;top:737px" width="58" height="50" viewBox="0 0 58 50">
    <path d="M29 3 L55 47 H3 Z"/>
    <path d="M32 16 L23 31 H30 L26 42 L36 27 H29 Z"/>
  </svg>
  <section class="service" style="left:471px;top:706px">
    <h3 class="service-name">High risk Electrical inspections</h3>
    <p class="service-text">All Prescribed Electrical Work that falls<br>under the High Risk category must be<br>inspected by a Registered Electrical<br>Inspector and have a Record of Inspection<br>certificate issued.</p>
  </section>
  <div class="service-rule" style="left:412px;top:861px;width:349px"></div>

  <svg class="service-icon" style="left:339px;top:911px" width="50" height="58" viewBox="0 0 50 58">
    <rect x="8" y="3" width="26" height="48" rx="2"/>
    <rect x="12" y="8" width="18" height="12"/>
    <path d="M22 25 L16 36 H22 L19 45 L27 33 H21 Z"/>
    <line x1="3" y1="55" x2="39" y2="55"/>
    <path d="M34 14 H40 Q44 14 44 18 V40 Q44 44 40 44 H36"/>
    <line x1="42" y1="4" x2="42" y2="10"/><line x1="46" y1="4" x2="46" y2="10"/>
  </svg>
  <section class="service" style="left:394px;top:872px">
    <h3 class="service-name">Electric Vehicle Chargers</h3>
    <p class="service-text">Any electrical vehicle charger that can be<br>accessed by the public (ie in a non-domestic<br>situation) must be periodically inspected<br>and certified every 12 months.</p>
  </section>
  <div class="service-rule" style="left:412px;top:1005px;width:349px"></div>

  <svg class="service-icon" style="left:404px;top:1046px" width="54" height="74" viewBox="0 0 54 74">
    <path d="M36 2 L4 46 H24 L16 72 L50 26 H30 Z"/>
  </svg>
  <section class="service" style="left:471px;top:1022px">
    <h3 class="service-name">General Electrical Services</h3>
    <p class="service-text">Domestic and commercial - We do new<br>builds, Renovations, Maintenance and<br>more!</p>
  </section>
  <div class="service-rule" style="left:412px;top:1152px;width:349px"></div>

  <h2 class="section-title about-title">About Us</h2>
  <p class="about-text">Lorem ipsum dolor sit amet, consectetur adipiscing elit, sed do eiusmod tempor incididunt ut labore et dolore magna aliqua. Quis ipsum suspendisse ultrices gravida. Risus commodo viverra maecenas accumsan lacus vel facilisis.</p>

  <h2 class="section-title contact-title">Contact Us</h2>
  <p class="contact-details">Dean Fowler - Electrician and<br>Electrical Inspector<br>Ph - 0227839152<br>Dean@voltarey.co.nz<br>Auckland</p>
  <div class="social">
    <span class="social-dot"></span>
    <span class="social-dot"><svg width="14" height="10" viewBox="0 0 14 10"><rect x="0.75" y="0.75" width="12.5" height="8.5" fill="none" stroke="#fff" stroke-width="1.3"/><polyline points="1,1 7,6 13,1" fill="none" stroke="#fff" stroke-width="1.3"/></svg></span>
    <span class="social-dot"></span>
    <span class="social-dot"></span>
  </div>
</main>
</body>
</html>
```